The Maplewick Academy Web Page

We need a web design for our Day Care Center based in Brandon, Florida. We are targeting child care and educational services to middle class parents, specially the mother. We would like to see designs that matches attached logo mark. The final design should communicate higher standards for day care and educational services.

Target Market(s)

Middle class parents in the State of Florida

Coding

Number of Pages Required

5+ page

```html
<!DOCTYPE html>
<html lang="en">
<head>
<meta charset="utf-8">
<title>The Maplewick Academy</title>
<link href="https://fonts.googleapis.com/css2?family=Raleway:wght@400;500;600&family=Arimo:wght@400;700&display=swap" rel="stylesheet">
<style>
:root{
  --yellow:#fbb934;
  --gold:#e8a322;
  --navy:#0c2341;
  --grey-bg:#f3f3f3;
  --text:#8a8a8a;
  --dark:#222;
  --line:#dcdcdc;
}
*{box-sizing:border-box;margin:0;padding:0}
html,body{width:1200px;height:2332px;overflow:hidden}
body{position:relative;background:#fff;font-family:"Arimo",Arial,sans-serif;color:var(--dark)}
.abs{position:absolute}

/* header */
.topbar{left:0;top:0;width:1200px;height:106px;background:var(--yellow)}
.brand{left:100px;top:22px;display:flex;align-items:center;gap:12px;z-index:3}
.brand-dot{width:26px;height:26px;border-radius:50%;background:var(--navy)}
.brand-name{font-family:"Raleway",sans-serif;font-weight:600;font-size:22px;color:var(--navy)}
.phone{left:625px;top:56px;font-family:"Raleway",sans-serif;font-size:21px;color:#fff}
.phone b{font-weight:500;margin-left:8px}
.social{left:962px;top:52px;display:flex;gap:8px}
.social span{width:31px;height:31px;border-radius:50%;background:#fff}
.social span:nth-child(2){background:var(--navy)}
.navbar{left:0;top:106px;width:1200px;height:49px;background:var(--navy)}
.nav{right:98px;top:123px;display:flex;gap:24px;font-size:14.5px;color:#fff;letter-spacing:.2px}
.nav .active{color:var(--yellow)}

/* hero */
.hero{left:0;top:155px;width:1200px;height:513px;background:linear-gradient(100deg,#d9d2c6 0%,#f1d7c1 30%,#e6b8a0 55%,#c9a592 75%,#7fa0c4 100%)}
.hero-rule{left:0;top:668px;width:1200px;height:4px;background:#f7d48c}
.hero-box{left:552px;top:412px;width:528px;height:180px;background:rgba(255,255,255,.55);padding:30px 22px}
.hero-title{font-family:"Raleway",sans-serif;font-size:22px;font-weight:500;color:var(--navy);letter-spacing:.3px}
.hero-tag{display:inline-block;margin-top:10px;background:var(--yellow);padding:9px 12px;width:324px;font-family:"Raleway",sans-serif;font-size:22px;color:var(--navy)}
.hero-tag em{font-style:normal;color:#fff}
.btn-light{display:inline-block;margin-top:12px;background:#fff;padding:9px 18px;font-size:14px;font-weight:700;color:var(--navy)}

/* features */
.features{left:0;top:672px;width:1200px;height:436px;background:linear-gradient(#fff,var(--grey-bg))}
.card{top:799px;width:280px;height:228px;background:#fff;border:1px solid var(--line);text-align:center;padding:50px 16px 0}
.card h3{font-family:"Raleway",sans-serif;font-weight:500;font-size:22px;color:var(--gold);margin-bottom:12px}
.card p{font-size:13px;line-height:17.5px;color:var(--text)}
.card ul{list-style:none;text-align:left;font-size:13px;line-height:17px;color:var(--text);padding:0 4px}
.card li{padding-left:14px;position:relative;padding-bottom:10px;margin-bottom:10px}
.card li:first-child{border-bottom:1px solid #e6e6e6}
.card li::before{content:"";position:absolute;left:2px;top:7px;width:5px;height:5px;border-radius:50%;background:#aaa}
.card .btn{position:absolute;left:50%;transform:translateX(-50%);bottom:-14px;width:124px;height:36px;line-height:36px;font-size:14px;color:#fff;background:var(--navy)}
.card .btn.gold{background:var(--gold)}
.icon-ring{top:707px;width:127px;height:127px;border-radius:50%;background:#e6e6e6;display:flex;align-items:center;justify-content:center}
.icon-ring div{width:108px;height:108px;border-radius:50%;background:#fff;display:flex;align-items:center;justify-content:center}

/* services */
.section-title{width:1200px;left:0;text-align:center;font-family:"Raleway",sans-serif;font-weight:500;color:var(--dark)}
.tabs{left:109px;top:1225px;width:984px;height:41px;display:flex;font-size:14.5px}
.tab{height:41px;line-height:41px;padding:0 20px;color:var(--dark)}
.tab.active{border:1px solid var(--line);border-bottom:1px solid #fff;background:#fff;position:relative;z-index:2;width:230px;text-align:center}
.panel{left:109px;top:1265px;width:984px;height:278px;border:1px solid var(--line)}
.svc-img{left:124px;top:1301px;width:348px;height:198px;border:8px solid #e4e4e4;background:linear-gradient(120deg,#c9a7e0,#f4d2c5 45%,#f5e9a8 75%,#c6d9f0)}
.svc-text{left:496px;top:1301px;width:580px}
.svc-text h3{font-family:"Raleway",sans-serif;font-weight:400;font-size:28px;color:var(--gold);margin-bottom:8px}
.svc-text p{font-size:15px;line-height:20px;color:#666}
.btn-navy{display:inline-block;margin-top:14px;background:var(--navy);color:#fff;font-size:15px;padding:8px 16px;border-radius:4px}

/* staff */
.staff{left:0;top:1591px;width:1200px;height:386px;background:var(--navy);color:#fff;text-align:center}
.staff h2{position:absolute;top:36px;width:100%;font-family:"Raleway",sans-serif;font-weight:500;font-size:25px}
.staff .intro{position:absolute;top:76px;left:230px;width:740px;font-size:15px;line-height:20px;color:#e8e8e8}
.member{position:absolute;top:160px;width:240px;text-align:center}
.avatar{width:117px;height:117px;margin:0 auto;border-radius:50%;border:4px solid var(--yellow);background:linear-gradient(#d9b8a4,#a88574)}
.member h4{margin-top:16px;font-weight:400;font-size:16px}
.member small{display:block;margin-top:8px;font-size:12px;font-style:italic;color:var(--yellow)}

/* activities */
.acts-title{top:2036px;font-size:23px}
.acts-title em{font-style:normal;color:var(--gold)}
.thumb{top:2100px;width:217px;height:135px}
.arrow{top:2150px}

/* footer */
.footer{left:0;top:2281px;width:1200px;height:51px;background:var(--yellow);text-align:center;line-height:51px;font-size:14px;color:var(--navy)}
</style>
</head>
<body>

<header>
  <div class="abs topbar"></div>
  <div class="abs navbar"></div>
  <div class="abs brand"><span class="brand-dot"></span><span class="brand-name">The Maplewick Academy</span></div>
  <div class="abs phone">Call Us Toll On <b>+1 813 555 0148</b></div>
  <div class="abs social" aria-label="Social links"><span></span><span></span><span></span><span></span></div>
  <nav class="abs nav">
    <span class="active">HOME</span><span>ADDMISSIONS</span><span>PHILOSOPHY</span><span>PROGRAMS</span><span>SERVICES</span><span>CAMPUSES</span><span>FRANCHISES</span>
  </nav>
</header>

<section>
  <div class="abs hero" role="img" aria-label="Photo of a mother and a young girl drawing with coloured pencils"></div>
  <div class="abs hero-rule"></div>
  <div class="abs hero-box">
    <div class="hero-title">INTRODUCING THE MAPLEWICK ACADEMY</div>
    <div class="hero-tag"><em>PREMIUM</em> CHILD CARE</div><br>
    <span class="btn-light">Read More</span>
  </div>
</section>

<section>
  <div class="abs features"></div>

  <div class="abs card" style="left:151px">
    <h3>Our Programs</h3>
    <p>Lorem Ipsum is simply dummy text of the printing and typesetting industry. Lorem Ipsum has been the Praesent arcu gravi vehicula est node maece-nas loareet morbi a dosis luctus.</p>
    <span class="btn">Read More</span>
  </div>
  <div class="abs card" style="left:460px">
    <h3>Our Mission</h3>
    <p>Lorem Ipsum is simply dummy text of the printing and typesetting industry. Lorem Ipsum has been the Praesent arcu gravi vehicula est node maece-nas loareet morbi a dosis luctus.</p>
    <span class="btn gold">Read More</span>
  </div>
  <div class="abs card" style="left:769px">
    <h3>Our Vision</h3>
    <ul><li>Lorem Ipsum is simply dummy text of the printing.</li><li>Lorem Ipsum is simply dummy text of the printing.</li></ul>
    <span class="btn">Read More</span>
  </div>

  <div class="abs icon-ring" style="left:227px"><div>
    <svg width="50" height="46" viewBox="0 0 50 46" fill="#0c2341">
      <rect x="1" y="1" width="12" height="12" fill="none" stroke="#0c2341" stroke-width="2"/>
      <rect x="18" y="1" width="12" height="12"/><rect x="35" y="17" width="12" height="12"/>
      <rect x="1" y="17" width="12" height="12"/><rect x="18" y="17" width="12" height="12"/>
      <rect x="1" y="33" width="12" height="12"/><rect x="18" y="33" width="12" height="12"/><rect x="35" y="33" width="12" height="12"/>
    </svg></div></div>
  <div class="abs icon-ring" style="left:536px"><div>
    <svg width="62" height="48" viewBox="0 0 62 48" fill="#0c2341">
      <path d="M4 20 L40 6 L44 38 L8 30 Z"/>
      <rect x="0" y="20" width="8" height="11" rx="2"/>
      <path d="M14 31 L20 44 L26 44 L22 33 Z"/>
      <path d="M48 12 L56 6 M50 22 L60 22 M48 32 L56 38" stroke="#0c2341" stroke-width="3" stroke-linecap="round"/>
    </svg></div></div>
  <div class="abs icon-ring" style="left:845px"><div>
    <svg width="58" height="34" viewBox="0 0 58 34">
      <path d="M2 17 C14 2 44 2 56 17 C44 32 14 32 2 17 Z" fill="none" stroke="#0c2341" stroke-width="4"/>
      <circle cx="29" cy="17" r="9" fill="#0c2341"/>
      <circle cx="26" cy="14" r="3" fill="#fff"/>
    </svg></div></div>
</section>

<section>
  <h2 class="abs section-title" style="top:1150px;font-size:25px">SERVICES OF THE MAPLEWICK ACADEMY</h2>
  <div class="abs panel"></div>
  <div class="abs tabs">
    <span class="tab" style="width:230px">Home School Support</span>
    <span class="tab active">School Readiness Provider</span>
    <span class="tab" style="width:230px;text-align:center">Voluntary Pre-K (VPK)</span>
    <span class="tab" style="width:230px;text-align:center">Enrichment Services</span>
  </div>
  <div class="abs svc-img" role="img" aria-label="Photo of a smiling girl with pigtails lying on a colourful play mat"></div>
  <div class="abs svc-text">
    <h3>School Readiness Provider</h3>
    <p>Praesent arcu gravida vehicula est node maecenas loareet morbi a dosis luctus. Urna eget lacinia eleifend praesent luctus a arcu quis facilisis venenatis aenean interdum.Praesent arcu gravida vehicula est node maecenas loareet morbi a dosis luctus. Urna eget lacinia eleifend praesent luctus a arcu quis facilisis venenatis aenean interdum.</p>
    <span class="btn-navy">Read More</span>
  </div>
</section>

<section class="abs staff">
  <h2>OUR STAFF</h2>
  <p class="intro">Praesent arcu gravida vehicula est node maecenas loareet morbi a dosis luctus. Urna eget lacinia eleifend praesent luctus a arcu quis facilisis venenatis aenean interdum.</p>
  <div class="member" style="left:140px"><div class="avatar" role="img" aria-label="Portrait photo of a staff member"></div><h4>Helen Marsh</h4><small>Sed diam nonummy nibh eusismod</small></div>
  <div class="member" style="left:455px"><div class="avatar" role="img" aria-label="Portrait photo of a staff member"></div><h4>Laura Penfold</h4><small>diam nonummy nibh eusismod tinc</small></div>
  <div class="member" style="left:750px"><div class="avatar" role="img" aria-label="Portrait photo of a staff member" style="background:linear-gradient(#9a6f55,#6b4a3a)"></div><h4>Nadia Corwin</h4><small>nonummy nibh eusismod tincidunt ut</small></div>
</section>

<section>
  <h2 class="abs section-title acts-title">OUR ACADEMY PROVIDES <em>PHYSICAL</em> AS WELL AS <em>MENTAL ACTIVITIES</em></h2>
  <svg class="abs arrow" style="left:98px" width="16" height="30" viewBox="0 0 16 30"><path d="M14 1 L2 15 L14 29" fill="none" stroke="#999" stroke-width="1.5"/></svg>
  <svg class="abs arrow" style="left:1086px" width="16" height="30" viewBox="0 0 16 30"><path d="M2 1 L14 15 L2 29" fill="none" stroke="#999" stroke-width="1.5"/></svg>
  <div class="abs thumb" style="left:140px;background:linear-gradient(135deg,#c7b3a0,#7fa1c8 60%,#d8c7b0)" role="img" aria-label="Photo of a teacher playing with toddlers at a table"></div>
  <div class="abs thumb" style="left:377px;background:linear-gradient(135deg,#c88f8f,#e8c7b8 50%,#a9b9d1)" role="img" aria-label="Photo of a toddler playing with blocks"></div>
  <div class="abs thumb" style="left:615px;background:linear-gradient(135deg,#7fb06a,#e5d26b 45%,#d5544a 80%)" role="img" aria-label="Photo of children on an indoor slide"></div>
  <div class="abs thumb" style="left:850px;background:linear-gradient(135deg,#d8c9b7,#c44a4a 50%,#6aa86a)" role="img" aria-label="Photo of a boy playing in a classroom"></div>
</section>

<footer class="abs footer">Copyright © 2015 The Maplewick Academy.</footer>

</body>
</html>
```